Pine Hollow toothpaste tube design

Design a Pine Hollow tube design for our all natural toothpaste. The toothpaste is 100% natural with a smooth marshmallow consistency. It's unique because it's not pastelike at all. The all natural flavors make the toothpaste taste great. The toothpaste is smooth yet still leaves your mouth feeling squeaky clean. We want to market this as an all natural family toothpaste.

The flavor is Mint. (possibly called "Koda Fern")

We have included our logo (eps & jpg), information that goes on the back of the tube, and the artwork template from the tube supplier for the 4.2oz tube.

We like a vintage earthy retro look and feel but we are not limited to this.

The tubes stand upright as shown in the picture of File 4.
Updates

The finished artwork must include anĀ adobe illustratorĀ file.

Project Deadline Extended

I would like to thank all of the designers for their work on this project. We had a difficult time making a decision since all of the designs were very close to what we expected.

Sincerely,

Rolf

Target Market(s)

The target market is families that desire an all natural toothpaste. We will be stressing the 100% natural and great taste.

Requirements
Must have
• Three colors maximum due to tube manufacture restrictions.

Must have "100% natural" and "fluoride free" on front of tube. A reference to the great taste or flavor is also important.

Must say 4.2 oz on the front of the tube, centered, at the bottom.
Nice to have
• Fun, colorful packaging that will stand out. Go to your local store and stand in front of the tootpaste shelves, give us something different!
Should not have
• We do not want a lot of red or blue because these are predominate colors already in use on toothpaste tubes and boxes.

```html
<!DOCTYPE html>
<html lang="en">
<head>
<meta charset="utf-8">
<title>Pine Hollow – Koda Fern tube artwork</title>
<link href="https://fonts.googleapis.com/css2?family=Crimson+Text:ital,wght@0,400;0,700;1,700&display=swap" rel="stylesheet">
<style>
  :root {
    --canvas: #f4f5f3;
    --tube: #ffffff;
    --tube-edge: #e2e4e0;
    --green: #2f8a3b;
    --green-deep: #1f6a2d;
    --green-soft: #a8d09a;
    --green-mist: #c9e3bf;
    --ink-light: #ffffff;
    --ink-dark: #2b2b2b;
  }
  * { margin: 0; padding: 0; box-sizing: border-box; }
  html, body { width: 1200px; height: 898px; overflow: hidden; }
  body {
    background: var(--canvas);
    font-family: "Crimson Text", Georgia, serif;
    position: relative;
  }
  .tube-panel {
    position: absolute;
    top: 60px;
    width: 300px;
    height: 790px;
    background: var(--tube);
    border: 1px solid var(--tube-edge);
    border-radius: 6px;
    overflow: hidden;
  }
  .tube-front { left: 290px; }
  .tube-back { left: 620px; }

  .brand-name {
    position: absolute;
    left: 0; right: 0;
    text-align: center;
    font-weight: 700;
    color: var(--green);
    line-height: 1;
  }
  .tube-front .brand-name { top: 120px; font-size: 46px; }
  .tube-back .brand-name { top: 80px; font-size: 32px; }

  .flavor-block {
    position: absolute;
    left: 12px; right: 12px;
    top: 250px;
    height: 345px;
  }
  .flavor-claim {
    height: 100px;
    background: var(--green-soft);
    color: var(--ink-light);
    font-weight: 700;
    font-size: 17px;
    line-height: 1.15;
    text-align: center;
    padding: 16px 30px 0 60px;
  }
  .flavor-name {
    height: 48px;
    background: var(--green);
    color: var(--ink-light);
    font-weight: 700;
    font-style: italic;
    font-size: 28px;
    line-height: 46px;
    text-align: center;
    letter-spacing: 1px;
  }
  .leaf-art {
    display: block;
    width: 100%;
    height: 197px;
  }
  .product-claims {
    position: absolute;
    right: 14px;
    top: 166px;
    text-align: right;
    color: var(--ink-light);
    font-weight: 700;
    font-size: 20px;
    line-height: 1.25;
    text-transform: uppercase;
    letter-spacing: 1px;
  }
  .cert-seal {
    position: absolute;
    left: 28px;
    top: 470px;
  }
  .net-weight {
    position: absolute;
    left: 0; right: 0;
    top: 612px;
    text-align: center;
    font-weight: 700;
    font-size: 22px;
    color: var(--ink-dark);
  }

  .label-copy {
    position: absolute;
    left: 34px; right: 34px;
    top: 150px;
    text-align: center;
    color: var(--green);
    font-size: 13.5px;
    line-height: 1.2;
  }
  .label-copy p { margin-bottom: 16px; }
  .label-copy .heading { display: block; }
</style>
</head>
<body>

  <section class="tube-panel tube-front" aria-label="Tube front">
    <div class="brand-name">Pine Hollow</div>

    <div class="flavor-block">
      <div class="flavor-claim">An all natural flavoured toothpaste for the whole family with a smooth, great taste.</div>
      <div class="flavor-name">Koda Fern</div>
      <svg class="leaf-art" viewBox="0 0 276 197" preserveAspectRatio="none" role="img" aria-label="Brush-textured illustration of large mint leaves in deep greens">
        <defs>
          <linearGradient id="leafTone" x1="0" y1="0" x2="1" y2="1">
            <stop offset="0" stop-color="#2f8a3b"/>
            <stop offset="1" stop-color="#1f6a2d"/>
          </linearGradient>
        </defs>
        <rect width="276" height="197" fill="url(#leafTone)"/>
      </svg>
      <div class="product-claims">100% Natural<br>Fluoride Free</div>
    </div>

    <svg class="cert-seal" width="90" height="90" viewBox="0 0 90 90" role="img" aria-label="Certification seal">
      <circle cx="45" cy="45" r="42" fill="var(--green-mist)" stroke="#ffffff" stroke-width="3"/>
    </svg>

    <div class="net-weight">4.2oz</div>
  </section>

  <section class="tube-panel tube-back" aria-label="Tube back">
    <div class="brand-name">Pine Hollow</div>

    <div class="label-copy">
      <p><span class="heading">Directions:</span>
        Adults and children 2 years of age and older: Brush teeth thoroughly, preferably after each meal or at least twice a day or as directed by a dentist. Children under 2: consult a dentist.</p>
      <p>Natural Ingredients: vegetable glycerin, de-ionized water, xylitol, calcium carbonate, USDA organic flavor concentrate, sodium coco-sulfate (derived from coconut oil), and carrageenan (extracted from seaweed).</p>
      <p>No parabens, no gluten, no glycols, no SLS, no TEA, no formaldehyde, no artificial flavors, no artificial dye, no artificial sweetener, no dairy, no sorbitol, no saccharines, no peroxides, and no fluoride!</p>
      <p>Made in USA<br>
        Distribution &amp; Supply Facility:<br>
        Pine Hollow LLC<br>
        218 Alder Way<br>
        Brookfield, MI 48990<br>
        www.pinehollowcare.com<br>
        hello@pinehollowcare.com</p>
    </div>
  </section>

</body>
</html>
```